Freeze dried pet treats and chews packaging design

We are an Belgium based brand selling all natural treats and chews for pets. We are looking for a full color packaging design for a new line of freeze dried treats and chews for cats and dogs. The design should look familiar for our customers with our existing logo, but with a fresh new design especially for this new line. It should reflect our core values of natural, species appropriate food products without any additives or nasties.
The packaging will be a stand-up pouch with zipper, eurohole, easy open and with a window somewhere in the design to show the products inside. Please present your design as a mockup if possible.
Name of the product will be "Velmo Freeze Dried Bitzoos". Add icons to emphasize certain aspects of the product:
- 100% natural
- freeze dried (preserves all nutrients best)
- 100% mono protein
- without additives
- high in protein
- high in flavor
The design is a generic one for 12 different products, only one pouch will be produced and finished with 12 different round labels to indicate the protein source (beef, chicken, lamb, etc). You can include one of these stickers on your design to make the example complete. The sticker should have a separate color for every protein source to make it good distinguishable, an icon representing the protein source (see examples of existing packaging) and a round text around it with the protein source in text in Dutch, French and English (example: RUND - BŒUF - BEEF).
Important: after this design we need more designs for other new product lines, so the winner might get more out of this then only this one project!
High premium pet products
Petfood
- Fontastique, Roboto (used for logo and current designs), others welcome too

```html
<!DOCTYPE html>
<html lang="en">
<head>
<meta charset="utf-8">
<title>Velmo Freeze Dried Bitzoos – Pouch Front</title>
<link rel="stylesheet" href="https://fonts.googleapis.com/css2?family=Archivo+Black&family=Rubik:wght@700;800&display=swap">
<style>
  :root {
    --lime: #a6ce39;
    --purple: #662d91;
    --purple-dark: #5a2783;
    --white: #ffffff;
  }
  * { box-sizing: border-box; margin: 0; padding: 0; }
  html, body { width: 1200px; height: 1200px; overflow: hidden; }
  body { background: var(--lime); position: relative; font-family: "Rubik", Arial, sans-serif; }

  .pouch-front {
    position: absolute; left: 300px; top: 180px;
    width: 600px; height: 841px;
    background: var(--purple);
  }
  .brand-band {
    position: absolute; left: 0; top: 153px; width: 100%; height: 53px;
    background: var(--lime);
  }
  .brand-tile {
    position: absolute; left: 399px; top: 103px; width: 148px; height: 125px;
    background: var(--white); border-radius: 10px;
    display: flex; align-items: center; justify-content: center;
  }
  .brand-name {
    font-family: "Rubik", Arial, sans-serif; font-weight: 700;
    font-size: 40px; color: var(--purple); letter-spacing: 0.5px;
  }
  .product-title {
    position: absolute; right: 53px; top: 262px;
    font-family: "Archivo Black", "Arial Black", sans-serif;
    font-size: 78px; line-height: 83px; color: var(--white);
    text-align: right; text-transform: uppercase;
  }
  .benefit-list {
    position: absolute; left: 100px; top: 540px; list-style: none;
    font-weight: 800; font-size: 20px; line-height: 25px; color: var(--white);
  }
  .benefit-list li::before { content: "• "; }
  .benefit-list .highlight { color: var(--lime); }

  .product-window {
    position: absolute; left: 502px; top: 532px; width: 35px; height: 200px;
    background: var(--white); border-radius: 14px;
  }
  .protein-label {
    position: absolute; left: 366px; top: 620px; width: 106px; height: 52px;
    border: 2px solid var(--lime); background: var(--purple);
    display: flex; flex-direction: column; text-align: center;
  }
  .protein-label__title {
    flex: 1; color: var(--white); font-weight: 800; font-size: 11px; line-height: 13px;
    padding-top: 4px;
  }
  .protein-label__source {
    background: var(--lime); color: var(--purple); font-weight: 800;
    font-size: 7.5px; line-height: 13px;
  }
  .species-marks {
    position: absolute; left: 374px; top: 694px; display: flex; gap: 10px;
  }
  .species-mark { width: 38px; height: 38px; border-radius: 50%; background: var(--white); }

  .feature-icons {
    position: absolute; left: 160px; top: 760px; display: flex; gap: 7px;
  }
  .feature-icons svg { width: 40px; height: 40px; display: block; }
</style>
</head>
<body>
  <main class="pouch-front">
    <div class="brand-band"></div>
    <div class="brand-tile"><span class="brand-name">Velmo</span></div>

    <h1 class="product-title">Freeze<br>Dried<br>Bitzoos</h1>

    <ul class="benefit-list">
      <li class="highlight">100% Natural</li>
      <li class="highlight">Freeze Dried</li>
      <li class="highlight">100% Mono Protein</li>
      <li>No Additives</li>
      <li>High Protein</li>
      <li>High in Flavor</li>
    </ul>

    <div class="product-window"></div>

    <div class="protein-label">
      <div class="protein-label__title">PROTEIN<br>SOURCE</div>
      <div class="protein-label__source">RUND – BŒUF – BEEF</div>
    </div>

    <div class="species-marks">
      <div class="species-mark" role="img" aria-label="Dog pictogram"></div>
      <div class="species-mark" role="img" aria-label="Cat pictogram"></div>
    </div>

    <div class="feature-icons">
      <svg viewBox="0 0 40 40" aria-label="100% natural">
        <rect x="2" y="2" width="36" height="36" rx="6" fill="none" stroke="#fff" stroke-width="3"/>
        <path d="M9 28 C10 14 22 10 31 11 C30 22 22 30 9 28 Z" fill="#fff"/>
      </svg>
      <svg viewBox="0 0 40 40" aria-label="Freeze dried">
        <rect x="2" y="2" width="36" height="36" rx="6" fill="none" stroke="#fff" stroke-width="3"/>
        <g stroke="#fff" stroke-width="2.5" stroke-linecap="round">
          <line x1="20" y1="9" x2="20" y2="31"/><line x1="10.5" y1="14.5" x2="29.5" y2="25.5"/><line x1="10.5" y1="25.5" x2="29.5" y2="14.5"/>
        </g>
      </svg>
      <svg viewBox="0 0 40 40" aria-label="100% mono protein">
        <rect x="2" y="2" width="36" height="36" rx="6" fill="none" stroke="#fff" stroke-width="3"/>
        <text x="20" y="17" text-anchor="middle" fill="#fff" font-family="Rubik, sans-serif" font-weight="800" font-size="10">100%</text>
        <path d="M9 29 l4 -6 l4 6 l4 -6 l4 6 l4 -6" fill="none" stroke="#fff" stroke-width="2.5"/>
      </svg>
      <svg viewBox="0 0 40 40" aria-label="No additives">
        <rect x="2" y="2" width="36" height="36" rx="6" fill="none" stroke="#fff" stroke-width="3"/>
        <rect x="15" y="11" width="10" height="19" rx="2" fill="none" stroke="#fff" stroke-width="2.5"/>
        <line x1="9" y1="31" x2="31" y2="9" stroke="#fff" stroke-width="2.5" stroke-linecap="round"/>
      </svg>
      <svg viewBox="0 0 40 40" aria-label="High protein">
        <rect x="2" y="2" width="36" height="36" rx="6" fill="none" stroke="#fff" stroke-width="3"/>
        <path d="M13 18 V9 M10 12 l3 -3 l3 3 M27 18 V9 M24 12 l3 -3 l3 3" fill="none" stroke="#fff" stroke-width="2.5" stroke-linecap="round"/>
        <path d="M9 30 l4 -6 l4 6 l4 -6 l4 6 l4 -6" fill="none" stroke="#fff" stroke-width="2.5"/>
      </svg>
      <svg viewBox="0 0 40 40" aria-label="High in flavor">
        <rect x="2" y="2" width="36" height="36" rx="6" fill="none" stroke="#fff" stroke-width="3"/>
        <path d="M12 15 V8 M9 11 l3 -3 l3 3 M28 15 V8 M25 11 l3 -3 l3 3" fill="none" stroke="#fff" stroke-width="2.5" stroke-linecap="round"/>
        <path d="M20 14 C24 20 26 23 26 26 A6 6 0 0 1 14 26 C14 23 16 20 20 14 Z" fill="none" stroke="#fff" stroke-width="2.5"/>
      </svg>
    </div>
  </main>
</body>
</html>
```